Lumex

Hello Artboardly Community,

Thank you for participating in designing Snapquill App. So far I've received some amazing looking designs!
Unfortunately, Some of the designs being submitted are not following the project brief.
The screens you submit should be designed "1:1 / Exactly" according to the project brief.
Updates

Target Market(s)

Millennials

Industry/Entity Type

Community

Font styles to use
Sans Serif

Requirements
Must have
• Follow the project brief exactly.

```html
<!DOCTYPE html>
<html lang="en">
<head>
<meta charset="UTF-8">
<title>Snapquill App Screens</title>
<link rel="stylesheet" href="https://fonts.googleapis.com/css2?family=Poppins:wght@400&family=Roboto:wght@400&display=swap">
<style>
  :root {
    --backdrop: #1b3668;
    --brand-blue: #4a87f3;
    --brand-blue-light: #5d97f5;
    --brand-blue-dark: #4482f2;
    --status-blue: #4a87ea;
    --surface: #fafafa;
    --white: #ffffff;
    --cabinet: #e2e2e2;
    --heading-grey: #7a7a7a;
    --body-grey: #858585;
  }
  * { box-sizing: border-box; margin: 0; padding: 0; }
  html, body { width: 1200px; height: 1200px; overflow: hidden; }
  body { background: var(--backdrop); position: relative; font-family: "Roboto", sans-serif; }

  .screen {
    position: absolute;
    top: 262px;
    width: 379px;
    height: 675px;
    overflow: hidden;
    box-shadow: 0 18px 40px rgba(0, 0, 0, 0.3);
  }
  .screen--splash {
    left: 148px;
    background: linear-gradient(160deg, var(--brand-blue-light) 0%, var(--brand-blue-dark) 45%, var(--brand-blue-dark) 100%);
  }
  .screen--empty { left: 674px; background: var(--surface); }

  /* Splash */
  .splash-mark {
    position: absolute;
    left: 162px; top: 249px;
    width: 55px; height: 55px;
    background: var(--white);
    border-radius: 4px;
  }
  .splash-name {
    position: absolute;
    left: 0; right: 0; top: 338px;
    text-align: center;
    font-family: "Poppins", sans-serif;
    font-size: 32px;
    color: var(--white);
    line-height: 44px;
  }
  .next-button {
    position: absolute;
    left: 160px; top: 563px;
    width: 60px; height: 60px;
    border-radius: 50%;
    background: var(--white);
    display: flex; align-items: center; justify-content: center;
  }

  /* Empty state screen */
  .status-bar {
    height: 26px;
    background: var(--status-blue);
    display: flex; align-items: center; justify-content: flex-end;
    gap: 8px;
    padding-right: 12px;
    color: var(--white);
    font-size: 12px;
  }
  .app-bar {
    height: 56px;
    background: var(--brand-blue);
    position: relative;
    box-shadow: 0 2px 4px rgba(0, 0, 0, 0.18);
  }
  .app-bar__menu { position: absolute; left: 21px; top: 20px; }
  .app-bar__title {
    position: absolute; left: 51px; top: 0;
    line-height: 56px;
    font-family: "Poppins", sans-serif;
    font-size: 19px;
    color: var(--white);
  }
  .app-bar__doc { position: absolute; left: 311px; top: 17px; }
  .app-bar__more { position: absolute; left: 353px; top: 17px; }

  .empty-state__art {
    position: absolute;
    left: 142px; top: 242px;
    width: 93px; height: 96px;
    background: var(--cabinet);
  }
  .empty-state__title {
    position: absolute; left: 0; right: 0; top: 353px;
    text-align: center;
    font-size: 20px;
    color: var(--heading-grey);
  }
  .empty-state__text {
    position: absolute; left: 0; right: 0; top: 388px;
    text-align: center;
    font-size: 13.5px;
    line-height: 17px;
    color: var(--body-grey);
  }
  .capture-button {
    position: absolute;
    left: 290px; top: 576px;
    width: 60px; height: 60px;
    border-radius: 50%;
    background: var(--brand-blue);
    box-shadow: 0 4px 8px rgba(0, 0, 0, 0.25);
    display: flex; align-items: center; justify-content: center;
  }
</style>
</head>
<body>

  <section class="screen screen--splash">
    <div class="splash-mark"></div>
    <h1 class="splash-name">Snapquill</h1>
    <div class="next-button">
      <svg width="20" height="24" viewBox="0 0 20 24"><path d="M6 3 L15 12 L6 21" fill="none" stroke="#4a87f3" stroke-width="2.4" stroke-linecap="round" stroke-linejoin="round"/></svg>
    </div>
  </section>

  <section class="screen screen--empty">
    <div class="status-bar">
      <svg width="16" height="14" viewBox="0 0 16 14"><path d="M1 13h2v-2H1zM5 13h2V8H5zM9 13h2V5H9zM13 13h2V1h-2z" fill="#ffffff"/></svg>
      <svg width="9" height="14" viewBox="0 0 9 14"><rect x="0" y="1.5" width="9" height="12.5" rx="1" fill="#ffffff"/><rect x="3" y="0" width="3" height="2" fill="#ffffff"/></svg>
      <span class="status-bar__time">12:30</span>
    </div>
    <header class="app-bar">
      <svg class="app-bar__menu" width="18" height="14" viewBox="0 0 18 14"><path d="M0 2h18M0 7h18M0 12h18" stroke="#ffffff" stroke-width="2"/></svg>
      <span class="app-bar__title">Snapquill</span>
      <svg class="app-bar__doc" width="18" height="22" viewBox="0 0 18 22"><path d="M2 0h9l7 7v13a2 2 0 0 1-2 2H2a2 2 0 0 1-2-2V2a2 2 0 0 1 2-2z" fill="#ffffff"/><path d="M11 0v7h7" fill="#d6e4fc"/></svg>
      <svg class="app-bar__more" width="6" height="22" viewBox="0 0 6 22"><circle cx="3" cy="3" r="2.3" fill="#ffffff"/><circle cx="3" cy="11" r="2.3" fill="#ffffff"/><circle cx="3" cy="19" r="2.3" fill="#ffffff"/></svg>
    </header>

    <div class="empty-state__art" role="img" aria-label="Illustration of an empty two-drawer filing cabinet"></div>
    <h2 class="empty-state__title">No Docments Uploaded yet</h2>
    <p class="empty-state__text">Lorem ipsum dolor sit amet, consectetur<br>adipisicing elit, sed do eiusmod tempor</p>

    <div class="capture-button">
      <svg width="26" height="22" viewBox="0 0 26 22"><path d="M3 5h5l2-3h6l2 3h5a2 2 0 0 1 2 2v12a2 2 0 0 1-2 2H3a2 2 0 0 1-2-2V7a2 2 0 0 1 2-2z" fill="#ffffff"/><circle cx="13" cy="12.5" r="4.5" fill="#4a87f3"/></svg>
    </div>
  </section>

</body>
</html>
```